California, rapidly growing Insurance Agency needs logo and letterhead design

we need a logo design and letterhead for an insurance company that specialize in providing businesses with insurance (workers comp , group health insurance, business insurance). I would like to see designs with a professional layout that use dark rich blues, and maybe some lighter blues mixed in. Also open to using grey and red tones. The design should communicate professional, yet current day feel (not too old/stuff or boring feel).
Updates

The company name is “Dovrel Insurance Services” If possible , would like to see a letterhead option with tag line worked in somewhere as “insurance specialist for over 45 years” Thank you!!!!

Target Market(s)

We insure businesses, do would like professional look with out being too stuffy or boring

Industry/Entity Type

Insurance Agency

Logo Text

Maybe “We make Insurance easy”

Font styles to use
Serif

Colors
3176b5
0993cd
f04b51

Requirements
Nice to have
• Would like to have rich dark blues and light mixed or also open to grey and
• Red color scheme
Should not have
• We target higher end clients, so would like to stay away from
• Any type of anime graphic

```html
<!DOCTYPE html>
<html lang="en">
<head>
<meta charset="utf-8">
<title>Dovrel Insurance Services — Letterhead</title>
<link href="https://fonts.googleapis.com/css2?family=Open+Sans:wght@400;600&family=Cinzel:wght@400&display=swap" rel="stylesheet">
<style>
  :root {
    --red: #f04b51;
    --grey-dark: #5f5f61;
    --ink: #333335;
    --text: #4a4a4c;
    --paper: #ffffff;
    --backdrop: #e4e4e6;
  }
  html, body {
    margin: 0;
    width: 1040px;
    height: 1200px;
    overflow: hidden;
    background: var(--backdrop);
    font-family: "Open Sans", Arial, sans-serif;
  }
  .letterhead {
    position: absolute;
    left: 53px;
    top: 0;
    width: 933px;
    height: 1200px;
    background: var(--paper);
    overflow: hidden;
    color: var(--text);
  }
  .brand {
    position: absolute;
    right: 91px;
    top: 36px;
    text-align: right;
  }
  .brand-name {
    display: flex;
    align-items: center;
    justify-content: flex-end;
    gap: 12px;
    font-family: "Cinzel", Georgia, serif;
    font-size: 30px;
    color: var(--red);
    letter-spacing: 1px;
    line-height: 1;
  }
  .brand-mark {
    width: 30px;
    height: 30px;
    background: var(--grey-dark);
  }
  .tagline {
    margin-top: 28px;
    font-size: 17.5px;
    color: var(--ink);
  }
  .letter-body {
    position: absolute;
    left: 88px;
    top: 216px;
    width: 755px;
    font-size: 15px;
  }
  .letter-body p { margin: 0; }
  .issue-date { margin-bottom: 20px !important; }
  .recipient { line-height: 18px; margin-bottom: 50px !important; }
  .salutation { margin-bottom: 26px !important; }
  .paragraph {
    line-height: 27px;
    text-align: justify;
    hyphens: auto;
    margin-bottom: 27px !important;
  }
  .closing { margin-top: 54px !important; margin-bottom: 58px !important; }
  .signatory-name { font-size: 19px; color: var(--ink); font-weight: 600; }
  .signatory-title { margin-top: 8px !important; }
  .footer-wave {
    position: absolute;
    left: 0;
    top: 0;
    width: 933px;
    height: 1200px;
  }
  .footer-address, .footer-contact {
    position: absolute;
    color: #fff;
    font-size: 17.5px;
    line-height: 22px;
  }
  .footer-address { left: 90px; top: 1139px; }
  .footer-contact { right: 95px; top: 1094px; text-align: right; }
  .contact-line { display: flex; align-items: center; justify-content: flex-end; gap: 5px; }
  .contact-line svg { width: 14px; height: 14px; }
</style>
</head>
<body>
<main class="letterhead">
  <header class="brand">
    <div class="brand-name"><span class="brand-mark"></span>Dovrel Insurance Services</div>
    <div class="tagline">Insurance specialist for over 45 years</div>
  </header>

  <section class="letter-body">
    <p class="issue-date">Issuing Date: May 5, 2018</p>
    <p class="recipient">Name Of Employee Mr. XYZABC<br>Address of Employee<br>Address Line 2 etc..</p>
    <p class="salutation">Dear Mr.XYZABC</p>
    <p class="paragraph">Lorem Ipsum has been the industry's standard dummy text ever since the 1500s, when an unknown printer took a galley of type and scrambled it to make a type specimen book. It has survived not only five centuries, but also the leap into electronic typesetting, remaining essentially unchanged. It was popularised in the 1960s with the release of Letraset sheets containing Lorem Ipsum passages, and more recently with desktop publishing software like Aldus PageMaker including versions of Lorem Ipsum.</p>
    <p class="paragraph">Lorem Ipsum is simply dummy text of the printing and typesetting industry. Lorem Ipsum has been the industry's standard dummy text ever since the 1500s, when an unknown printer took a galley of type and scrambled it to make a type specimen book.</p>
    <p class="paragraph">It has survived not only five centuries, but also the leap into electronic typesetting, remaining essentially unchanged. It was popularised in the 1960s with the release of Letraset sheets containing Lorem IpsumIpsum passages.</p>
    <p class="closing">Yours Sincerely</p>
    <p class="signatory-name">Marcus Hale</p>
    <p class="signatory-title">Managing Director</p>
  </section>

  <svg class="footer-wave" viewBox="0 0 790 1016" preserveAspectRatio="none" aria-hidden="true">
    <path d="M0 870 C60 900 140 925 240 925 C330 925 420 912 475 900 C400 915 320 930 230 930 C130 930 60 918 0 900 Z" fill="#5f5f61"/>
    <path d="M0 905 C70 925 150 935 240 935 C400 935 560 885 790 883 L790 1016 L0 1016 Z" fill="#f04b51"/>
  </svg>

  <div class="footer-address">12345, Address Goes Here<br>Country Name, 123456</div>
  <div class="footer-contact">
    <div class="contact-line">044-555 019 274
      <svg viewBox="0 0 16 16"><path d="M3 6c0-2 2-3 5-3s5 1 5 3v1h-3V5.5H6V7H3zM4 8h8l1 5H3z" fill="#fff"/></svg></div>
    <div class="contact-line">info@dovrelins.com
      <svg viewBox="0 0 16 16"><rect x="2" y="4" width="12" height="9" fill="#fff"/><path d="M2.5 4.5 8 9l5.5-4.5" stroke="#f04b51" stroke-width="1.2" fill="none"/></svg></div>
    <div class="contact-line">www.dovrelins.com
      <svg viewBox="0 0 16 16"><circle cx="8" cy="8" r="6" fill="#fff"/><path d="M5 6c1 0 2 1 2 2s2 1 2 3M9 3.5c0 1 1 2 2.5 2" stroke="#f04b51" stroke-width="1.3" fill="none"/></svg></div>
  </div>
</main>
</body>
</html>
```